Thank You Card design for a federal credit union

I am looking to have a thank you card designed.
Specs:
Flat size of 9.5"x6.5" folds to final size of 4.75"x6.5", it will print full color on the front and back. Below, you will see their logo, which needs to print on the inside of the folded card. I also attached images of their current card. They would like to keep the blue color but are open to design on the front. This is a Federal Credit Union, so please make the design, modern and professional. Below is the text that needs to print below the logo on the inside of the card. The text and logo will print below the fold on the inside, leave the top portion (above the panel) white.
Inside text:
Our Members are the foundation of our Credit Union. We sincerely thank you for your loyalty, your business and the opportunity to serve you.
Target Market(s)
Clients of a federal credit union
Industry/Entity Type
Union
Requirements
Must have
- a simple, professional, and modern feel. "Thank You for your business" must be on the front section in some variation.
Should not have
- nothing flashy or too many colors. keep it simple

```html
<!DOCTYPE html>
<html lang="en">
<head>
<meta charset="utf-8">
<title>Thank You Card – Front Panel</title>
<link href="https://fonts.googleapis.com/css2?family=Lobster&family=Lobster+Two:ital,wght@1,700&display=swap" rel="stylesheet">
<style>
  :root {
    --backdrop: #8a8a8c;
    --backdrop-light: #9a9a9c;
    --card-navy: #1a1a4a;
    --card-navy-deep: #181845;
    --card-navy-soft: #1f1f55;
    --ink-white: #ffffff;
  }
  html, body {
    margin: 0;
    padding: 0;
    width: 1200px;
    height: 1200px;
    overflow: hidden;
  }
  body {
    background: radial-gradient(circle at 50% 45%, var(--backdrop-light) 0%, var(--backdrop) 70%);
    display: flex;
    align-items: center;
    justify-content: center;
  }
  .card-front {
    position: relative;
    width: 1000px;
    height: 731px;
    background: var(--card-navy);
    box-shadow: 0 10px 30px rgba(0, 0, 0, 0.25);
    overflow: hidden;
  }
  .card-texture {
    position: absolute;
    inset: 0;
    background: linear-gradient(170deg, var(--card-navy-soft) 0%, var(--card-navy) 55%, var(--card-navy-deep) 100%);
  }
  .greeting {
    position: absolute;
    inset: 0;
    color: var(--ink-white);
  }
  .greeting__lead,
  .greeting__tail {
    position: absolute;
    font-family: "Lobster Two", "Lobster", cursive;
    font-style: italic;
    font-weight: 700;
    font-size: 44px;
    line-height: 1;
    white-space: nowrap;
  }
  .greeting__lead {
    left: 98px;
    top: 276px;
  }
  .greeting__main {
    position: absolute;
    left: 150px;
    top: 318px;
    font-family: "Lobster", cursive;
    font-size: 150px;
    line-height: 1;
    white-space: nowrap;
    letter-spacing: 1px;
  }
  .greeting__tail {
    left: 560px;
    top: 478px;
  }
</style>
</head>
<body>
  <main class="card-front">
    <div class="card-texture" role="img" aria-label="Faint geometric cube line pattern on navy background"></div>
    <div class="greeting">
      <p class="greeting__lead" style="margin:0">We would like to say</p>
      <h1 class="greeting__main" style="margin:0;font-weight:400">Thank You</h1>
      <p class="greeting__tail" style="margin:0">for your business</p>
    </div>
  </main>
</body>
</html>
```